Window Company website re-design

We are creating a new website design for http://harborpanes.example and we are going to be using wordpress for the site. The idea is to make it appeal to homeowners, more than half of the visitors will be female so the design must appeal to them with appropriate colors and shapes. Historically the website has been dark with a black background and the idea is to keep some of that but make it much brighter with textures and inviting colors.
Major competitors which we will mimic are the following in order of favorites:
http://www.birchvalleyglass.example/ (this is something we really like because of the full width, call to action, easy to navigate, space for
http://www.grainhillexteriors.example/ (this is a nice wide design with a lot of great image space and call to actions)
http://www.restorebyhollister.example/ (the full width is nice here)
http://www.duskpointpanes.example/ (the slide over option showing the window is nice here.)
Others:
http://www.torvane.example/
http://www.quiro.example/home/default.aspx
http://www.hollisterpanes.example/
https://www.glazeplanet.example/
http://www.delcot.example/

Harbor is the leader in the industry so they want a design that is going to portray that. The owners say that their competitors always copy what they do so this design must be cutting edge.

Important elements need to included:
1. Make the design convey very obviously they are a replacement window and door company.
2. Very clear “request a free estimate” call to action box on the homepage.
3. Area for the “Live Support” call to action
4. Navigation:

- Home
- Why Harbor
o Saves Dollars, Makes Sense
o We Have You Covered Start to Finish
o The Harbor Difference
o Pitfalls to Avoid
- Windows and Doors
o Windows
 Double Hung Windows
 Awning Windows
 Basement Hopper Windows
 Bow Windows
 Garden Windows
 Casement Windows
 Bay Windows
 Slider Windows
 Dead-Lite / Specialty / Transom
o Doors
 Storm Doors
 Harbor French Doors
 Patio Slider Doors
 Door Catalog
 Keypad Deadbolt
o Before and After
- About Us
o Testimonials
o Directions
o Warranty
o Employment
o Manufacturing process
o Home Shows
o Community Involvement
- Financing
- Commercial Division
- Careers
- Contact Us

Important elements for the Home Page:
1. Call to action – request a free quote
2. Awards
3. Live support
4. Guarantee
5. Featured testimonials
6. Press releases
7. Locations (Map?)

The attached photos can be used for the homepage images

Target Market(s)

The target market is middle income home owners who want good quality and great service.

Industry/Entity Type

Industry

Font styles to use
Sans Serif

Colors

Designer to choose colors to be used in the design.

Requirements
Must have
• We will need 2 designs, one for the homepage and the other for the inner pages.

2. Awards
3. Live support
4. Guarantee
5. Featured testimonials
6. Press releases
7. Locations (Map?)

```html
<!DOCTYPE html>
<html lang="en">
<head>
<meta charset="utf-8">
<title>Windows | Harbor</title>
<link rel="stylesheet" href="https://fonts.googleapis.com/css2?family=Open+Sans:wght@400;600;700&family=Josefin+Sans:wght@600;700&display=swap">
<style>
:root{
  --cream:#f3ead6;
  --green:#2e8b2a;
  --green-dark:#23701f;
  --ink:#333333;
  --muted:#666666;
  --panel:#f2f2f2;
  --white:#ffffff;
  --black:#111111;
  --footer:#1c1c1c;
  --footer-text:#cfcfcf;
}
*{box-sizing:border-box;margin:0;padding:0}
html,body{width:1200px;height:2672px;overflow:hidden}
body{position:relative;background:var(--white);font-family:"Open Sans",Arial,sans-serif;color:var(--ink)}
.abs{position:absolute}

/* header */
.top-band{left:0;top:0;width:1200px;height:227px;background:var(--cream)}
.header{left:140px;top:20px;width:920px;height:111px;background:var(--white)}
.brand{left:0;top:0;width:236px;height:111px}
.brand-name{position:absolute;left:34px;top:36px;display:flex;align-items:center;gap:12px;color:var(--white);font-weight:700;font-size:34px;line-height:1}
.brand-name .mark{width:22px;height:22px;background:var(--white)}
.util-nav{right:60px;top:18px;display:flex;gap:26px;font-size:14px;color:var(--muted);letter-spacing:.5px}
.search-btn{right:20px;top:14px;width:30px;height:30px;background:var(--green);display:flex;align-items:center;justify-content:center}
.main-nav{right:20px;top:72px;display:flex;gap:44px;font-size:15px;font-weight:600;color:var(--ink);letter-spacing:.3px}
.main-nav .active{color:var(--green)}
.main-nav .caret{color:var(--muted);font-size:11px;margin-left:6px}
.main-nav .active .caret{color:var(--green)}
.page-title{left:0;top:160px;width:1200px;text-align:center;font-family:"Josefin Sans",sans-serif;font-weight:700;font-size:34px;color:var(--green);letter-spacing:1px}
.title-rule{left:570px;top:199px;width:60px;height:3px;background:var(--green)}

.hero{left:0;top:227px;width:1200px;height:285px;background:linear-gradient(90deg,#7fb3e0 0%,#9a2f2c 22%,#a3302d 50%,#9a2f2c 78%,#8fc0e6 100%)}

.live-chat{left:1142px;top:283px;width:58px;height:167px;background:var(--green);border-radius:6px 0 0 6px}
.live-chat span{position:absolute;left:14px;top:150px;transform:rotate(-90deg);transform-origin:left top;color:var(--white);font-weight:700;font-size:19px;letter-spacing:1px;white-space:nowrap}

/* content */
.content{left:140px;top:559px;width:920px;height:1589px;background:var(--panel)}
.sidebar{left:162px;top:578px;width:260px}
.side-title{font-family:"Josefin Sans",sans-serif;font-weight:700;font-size:22px;color:var(--green-dark);letter-spacing:.5px;margin-bottom:6px}
.side-list{list-style:none}
.side-list li{font-size:15px;color:var(--muted);height:32px;line-height:32px}
.side-list li::before{content:"›";font-weight:700;color:var(--ink);margin-right:10px;font-size:18px}
.side-list li.current{color:var(--green)}
.award-banner{left:167px;top:806px;width:254px;height:182px;background:linear-gradient(135deg,#2fb6a5,#1d9a8a)}

.tile{width:307px;height:321px}
.tile .photo{width:307px;height:234px}
.tile .caption{height:87px;padding-top:24px;text-align:center;font-size:15px;font-weight:600;color:var(--ink)}
.tile.hover .caption{background:#3a3a3a;color:var(--white)}
.tile.hover .photo{position:relative;background:linear-gradient(160deg,#4a4a48,#2c2c2b)}
.plus{position:absolute;left:123px;top:87px;width:60px;height:60px}
.plus::before,.plus::after{content:"";position:absolute;background:rgba(255,255,255,.85)}
.plus::before{left:29px;top:0;width:2px;height:60px}
.plus::after{left:0;top:29px;width:60px;height:2px}

/* footer */
.footer{left:0;top:2188px;width:1200px;height:484px;background:var(--footer)}
.map{left:140px;top:2224px;width:441px;height:285px;background:linear-gradient(135deg,#f3efe2,#e8e3cf 60%,#f0d9a0)}
.newsletter{left:619px;top:2224px;width:441px;height:165px;background:var(--white);padding:16px 18px}
.newsletter h3{font-family:"Josefin Sans",sans-serif;font-weight:700;font-size:22px;color:var(--green-dark);letter-spacing:.5px}
.field-row{display:flex;gap:14px;margin-top:14px}
.field{width:196px;height:38px;background:#e9e9e9;border:1px solid #d6d6d6;font-size:13px;color:#999;padding:10px 8px}
.subscribe{display:inline-block;margin-top:14px;background:var(--green);color:var(--white);font-weight:700;font-size:16px;padding:8px 16px}
.contact{left:619px;top:2437px;color:var(--white);font-size:15px;line-height:30px}
.contact .phone{color:#4fc24a;font-size:24px;font-weight:700;vertical-align:-2px}
.cert-badge{left:919px;top:2427px;width:136px;height:80px;border-radius:50%;background:var(--green);border:4px solid #e8e8e8}
.footer-links{left:0;top:2542px;width:1200px;text-align:center;color:var(--footer-text);font-size:13px;line-height:26px}
.footer-rule{left:140px;top:2618px;width:920px;height:1px;background:#333}
.copyright{left:140px;top:2638px;font-size:13px;color:var(--footer-text)}
.social{left:911px;top:2634px;display:flex;gap:8px}
.social i{display:block;width:30px;height:30px}
</style>
</head>
<body>
<div class="abs top-band"></div>

<header class="abs header">
  <div class="abs brand">
    <svg width="236" height="111" style="position:absolute;left:0;top:0"><polygon points="0,0 236,0 190,111 0,111" fill="#111111"/></svg>
    <div class="brand-name"><span class="mark"></span>Harbor</div>
  </div>
  <nav class="abs util-nav"><span>HOME</span><span>CAREERS</span><span>FINANCING</span><span>CONTACT</span></nav>
  <div class="abs search-btn">
    <svg width="16" height="16" viewBox="0 0 16 16"><circle cx="6.5" cy="6.5" r="4.5" fill="none" stroke="#fff" stroke-width="2"/><line x1="10" y1="10" x2="14.5" y2="14.5" stroke="#fff" stroke-width="2.2"/></svg>
  </div>
  <nav class="abs main-nav">
    <span>WHY HARBOR<span class="caret">⌄</span></span>
    <span class="active">WINDOWS &amp; DOORS<span class="caret">⌄</span></span>
    <span>ABOUT US<span class="caret">⌄</span></span>
    <span>COMMERCIAL DIVISION</span>
  </nav>
</header>

<h1 class="abs page-title">WINDOWS</h1>
<div class="abs title-rule"></div>

<div class="abs hero" role="img" aria-label="Red two-storey house with white-trimmed replacement windows under a blue sky"></div>

<div class="abs live-chat">
  <svg width="26" height="22" viewBox="0 0 26 22" style="position:absolute;left:16px;top:10px"><path d="M3 2h20a2 2 0 0 1 2 2v10a2 2 0 0 1-2 2H11l-6 5v-5H3a2 2 0 0 1-2-2V4a2 2 0 0 1 2-2z" fill="#fff"/></svg>
  <span>LIVE CHAT</span>
</div>

<main class="abs content"></main>

<aside class="abs sidebar">
  <h2 class="side-title">DOORS</h2>
  <ul class="side-list">
    <li class="current">Storm Doors</li>
    <li>Harbor French Doors</li>
    <li>Patio Slider Doors</li>
    <li>Door Catalog</li>
    <li>Keypad Deadbolt</li>
  </ul>
</aside>
<div class="abs award-banner" role="img" aria-label="Award announcement banner with magazine clippings and a click here button"></div>

<div class="abs tile hover" style="left:445px;top:559px">
  <div class="photo" role="img" aria-label="Interior view of double hung windows"><div class="plus"></div></div>
  <div class="caption">Double Hung Windows</div>
</div>
<div class="abs tile" style="left:752px;top:559px">
  <div class="photo" role="img" aria-label="Beige house with awning windows" style="background:linear-gradient(180deg,#8fb8e0,#e8c9a0 55%,#6a9a4a)"></div>
  <div class="caption">Awning Windows</div>
</div>
<div class="abs tile" style="left:445px;top:880px">
  <div class="photo" role="img" aria-label="Empty room with basement hopper windows" style="background:linear-gradient(180deg,#e6e4de,#d8d4cb 60%,#a7895f)"></div>
  <div class="caption">Basement Hopper Windows</div>
</div>
<div class="abs tile" style="left:752px;top:880px">
  <div class="photo" role="img" aria-label="Brick house with bow window and flower bed" style="background:linear-gradient(180deg,#9a5a3c,#b06a45 55%,#5b7a3a)"></div>
  <div class="caption">Bow Windows</div>
</div>
<div class="abs tile" style="left:445px;top:1202px">
  <div class="photo" role="img" aria-label="White sided house with garden windows" style="background:linear-gradient(180deg,#c9d4dc,#e4e4e0 60%,#6d8a4c)"></div>
  <div class="caption">Garden Windows</div>
</div>
<div class="abs tile" style="left:752px;top:1202px">
  <div class="photo" role="img" aria-label="Stone wall with arched casement windows" style="background:linear-gradient(180deg,#7d7a70,#8a5a40 50%,#6e6a60)"></div>
  <div class="caption">Casement Windows</div>
</div>
<div class="abs tile" style="left:445px;top:1523px">
  <div class="photo" role="img" aria-label="Red roof with dormer bay windows" style="background:linear-gradient(180deg,#a8242a,#c23a34 60%,#d8cbb0)"></div>
  <div class="caption">Bay Windows</div>
</div>
<div class="abs tile" style="left:752px;top:1523px">
  <div class="photo" role="img" aria-label="Window seat beneath slider windows" style="background:linear-gradient(180deg,#d9cdb6,#c4b08e 55%,#efe9dc)"></div>
  <div class="caption">Slider Windows</div>
</div>
<div class="abs tile" style="left:445px;top:1843px">
  <div class="photo" role="img" aria-label="Bright living room with large specialty windows" style="background:linear-gradient(180deg,#d9d6cf,#c9c2b6 55%,#f2efe9)"></div>
  <div class="caption">Dead-Lite / Specialty / Transom</div>
</div>

<footer class="abs footer"></footer>
<div class="abs map" role="img" aria-label="Road map showing office locations"></div>
<div class="abs newsletter">
  <h3>NEWSLETTERS</h3>
  <div class="field-row"><div class="field">Enter Your Name</div><div class="field">Enter Your Email</div></div>
  <div class="subscribe">SUBSCRIBE</div>
</div>
<div class="abs contact">
  <div>Call Now : <span class="phone">800 555-0142</span></div>
  <div>Email : info@harborpanes.example</div>
</div>
<div class="abs cert-badge" role="img" aria-label="Certification badge"></div>
<nav class="abs footer-links">
  <div>Home | Before &amp; After | Home Shows | Financing | Directions | About Us | Warranty | FAQ | Contact Us | Employment | Estimate Request</div>
  <div>Community Involvement | Competitors Click Here | Tax Credit Info | Manufacturing Process | Commercial Division</div>
</nav>
<div class="abs footer-rule"></div>
<div class="abs copyright">Copyright 2014 by Harbor Windows &nbsp;/&nbsp; Harbor Windows &nbsp;/&nbsp; Privacy Statement &nbsp;/&nbsp; Terms Of Use</div>
<div class="abs social" aria-label="Social links">
  <i style="background:#3b5998"></i><i style="background:#2aa3d8"></i><i style="background:#0e76a8"></i><i style="background:#c4302b"></i>
</div>
</body>
</html>
```